Executive Business Card for Healthcare Company [Need Today]

I need a business card design for a healthcare company. The only branding the company has thus far is a logo. The cards will be utilized by company executives. The design I envision will be vibrant and appealing but with a corporate feel. They shouldn't be too casual or playful. I would like to complete this project TODAY if possible.

Target Market(s)

Healthcare vendors, other executives in healthcare and pharmaceuticals

Industry/Entity Type

Pharmaceutical

Contact Information for Business Card

See attachment

Font styles to use
Serif
Sans Serif

Colors

Designer to choose colors to be used in the design.

```html
<!DOCTYPE html>
<html lang="en">
<head>
<meta charset="utf-8">
<title>Veltra Therapeutics – Executive Business Card</title>
<link href="https://fonts.googleapis.com/css2?family=Questrial&display=swap" rel="stylesheet">
<style>
  :root {
    --teal: #36bfc6;
    --teal-deep: #2aa9b0;
    --grey: #6d6e71;
    --grey-light: #9a9b9e;
    --ink: #4a4b4d;
    --white: #ffffff;
    --backdrop: #2b2b2d;
    --logo-green: #5cc39a;
  }
  * { box-sizing: border-box; margin: 0; padding: 0; }
  html, body {
    width: 1200px; height: 880px; overflow: hidden;
    background: var(--backdrop);
    font-family: "Questrial", "Century Gothic", sans-serif;
  }
  .stage { position: relative; width: 1200px; height: 880px; }

  .card {
    position: absolute;
    width: 600px; height: 343px;
    border-radius: 22px;
    overflow: hidden;
    box-shadow: 0 14px 30px rgba(0,0,0,.45);
  }

  /* Front */
  .card--front { left: 150px; top: 60px; background: var(--teal); }
  .front__ring {
    position: absolute; left: -60px; top: 60px;
    width: 330px; height: 330px; border-radius: 50%;
    border: 22px solid rgba(0,0,0,.05);
  }
  .front__brand {
    position: absolute; left: 0; right: 0; top: 0; bottom: 0;
    display: flex; align-items: center; justify-content: center; gap: 16px;
  }
  .brand__dot {
    width: 78px; height: 78px; border-radius: 50%;
    border: 3px solid var(--white);
  }
  .brand__divider { width: 1px; height: 60px; background: rgba(255,255,255,.7); }
  .brand__name {
    font-size: 30px; line-height: 1.05; letter-spacing: .5px; color: var(--white);
  }
  .brand__name span { display: block; font-size: 30px; }

  /* Back */
  .card--back { left: 450px; top: 470px; background: var(--white); }
  .back__waves { position: absolute; inset: 0; }
  .back__person {
    position: absolute; right: 30px; top: 20px; text-align: right; color: var(--white);
  }
  .person__name { font-size: 22px; letter-spacing: .3px; }
  .person__title { font-size: 14px; margin-top: 2px; }

  .back__brand {
    position: absolute; left: 36px; top: 140px;
    display: flex; align-items: center; gap: 12px;
  }
  .back__brand .brand__dot { width: 74px; height: 74px; border-color: var(--logo-green); }
  .back__brand .brand__divider { background: var(--grey-light); height: 52px; }
  .back__brand .brand__name { color: var(--teal); font-size: 28px; }
  .back__brand .brand__name span { font-size: 28px; }

  .back__address {
    position: absolute; right: 30px; top: 150px; width: 240px;
    border-top: 1px solid var(--grey-light); padding-top: 12px;
    text-align: right; font-size: 14px; line-height: 1.4; color: var(--ink);
  }
  .address__company { color: var(--teal); }

  .back__contact {
    position: absolute; left: 36px; bottom: 22px; width: 300px;
    border-top: 1px solid var(--grey-light); padding-top: 10px;
    list-style: none; font-size: 15px; line-height: 1.45; color: var(--ink);
  }
  .back__contact li { display: flex; align-items: center; gap: 8px; }
  .contact__icon { width: 14px; height: 14px; flex: none; }
</style>
</head>
<body>
<main class="stage">

  <section class="card card--front" aria-label="Card front">
    <div class="front__ring"></div>
    <div class="front__brand">
      <div class="brand__dot"></div>
      <div class="brand__divider"></div>
      <div class="brand__name">veltra <span>therapeutics</span></div>
    </div>
  </section>

  <section class="card card--back" aria-label="Card back">
    <svg class="back__waves" width="600" height="343" viewBox="0 0 600 343">
      <path d="M0 0 H600 V98 C470 58 250 52 0 120 Z" fill="var(--teal)"/>
      <path d="M0 128 C250 60 470 66 600 112 V98 C470 58 250 52 0 120 Z" fill="var(--grey)"/>
    </svg>

    <div class="back__person">
      <div class="person__name">Martin Hale</div>
      <div class="person__title">Senior Director of Marketing</div>
    </div>

    <div class="back__brand">
      <div class="brand__dot"></div>
      <div class="brand__divider"></div>
      <div class="brand__name">veltra <span>therapeutics</span></div>
    </div>

    <div class="back__address">
      <div class="address__company">Veltra Therapeutics, LLC</div>
      <div>118 W Oak Avenue</div>
      <div>Dalton, GA 30720</div>
    </div>

    <ul class="back__contact">
      <li>
        <svg class="contact__icon" viewBox="0 0 14 14"><rect x="3" y="1" width="8" height="12" rx="1.5" fill="none" stroke="var(--teal)" stroke-width="1.4"/><circle cx="7" cy="11" r=".9" fill="var(--teal)"/></svg>
        555-210-4817
      </li>
      <li>
        <svg class="contact__icon" viewBox="0 0 14 14"><circle cx="7" cy="7" r="7" fill="var(--teal)"/><path d="M4 5.5 C4 4.5 10 4.5 10 5.5 L9 6.5 L8 6 L6 6 L5 6.5 Z M4.5 9.5 H9.5 L9 7.5 H5 Z" fill="var(--white)"/></svg>
        555-638-2940
      </li>
      <li>
        <svg class="contact__icon" viewBox="0 0 14 14"><circle cx="7" cy="7" r="7" fill="var(--teal)"/><rect x="3.5" y="4.5" width="7" height="5" fill="none" stroke="var(--white)" stroke-width="1"/><path d="M3.5 4.5 L7 7.5 L10.5 4.5" fill="none" stroke="var(--white)" stroke-width="1"/></svg>
        mhale@veltratx.com
      </li>
    </ul>
  </section>

</main>
</body>
</html>
```